Graphic Insert - For Pillow Case

We are purchasing new pillow cases for a campaign we are running and need a graphic insert as part of our corporate branding and product description to go in our packaging. The packaging will be a clear plastic back with this graphic insert.

Size of Flyer: 6"x9"

Description: 440 Thread Count Egyptian Cotton Pillow Cases
Quantity: 2
Size of Pillow Case: Standard
Descriptive Words: Soft, Caress, Smooth, Gentle

Our website: www.velardo.com

Thanks,

Dale

```html
<!DOCTYPE html>
<html lang="en">
<head>
<meta charset="utf-8">
<title>Velardo Sleep Products – Pillow Case Insert</title>
<link rel="stylesheet" href="https://fonts.googleapis.com/css2?family=Marcellus&family=Questrial&display=swap">
<style>
  :root {
    --olive-dark: #8d8f4f;
    --olive: #b5b36a;
    --olive-light: #d9d59a;
    --cream: #f4f1dc;
    --paper: #fbfaf2;
    --ink: #4e4e4e;
    --ink-soft: #5c5c5c;
    --brand-grey: #666666;
    --brand-olive: #8a8c4c;
    --linen-light: #f7f5ee;
    --linen: #efece3;
    --linen-warm: #ebe6d4;
  }
  html, body {
    margin: 0;
    padding: 0;
    width: 827px;
    height: 1200px;
    overflow: hidden;
    background: #ffffff;
  }
  .insert {
    position: relative;
    width: 827px;
    height: 1200px;
    box-sizing: border-box;
    border: 6px solid var(--olive-dark);
    background: linear-gradient(90deg, var(--olive) 0%, var(--olive-light) 11%, var(--cream) 11.2%, var(--paper) 50%, var(--cream) 87.8%, var(--olive-light) 88%, var(--olive) 100%);
    overflow: hidden;
    font-family: "Questrial", sans-serif;
    color: var(--ink);
  }
  .side-wash {
    position: absolute;
    inset: 0;
    background: linear-gradient(180deg, rgba(255,255,255,0.35) 0%, rgba(255,255,255,0) 40%, rgba(255,255,255,0.3) 70%, rgba(180,176,100,0.15) 100%);
  }
  .swoosh {
    position: absolute;
    inset: 0;
    width: 100%;
    height: 100%;
  }
  .brand {
    position: absolute;
    top: 100px;
    left: 114px;
    display: flex;
    align-items: center;
    gap: 24px;
  }
  .brand-dot {
    width: 172px;
    height: 172px;
    border-radius: 50%;
    border: 5px solid var(--brand-grey);
    box-sizing: border-box;
    flex: none;
  }
  .brand-words {
    display: flex;
    flex-direction: column;
    margin-top: 8px;
  }
  .brand-name {
    font-family: "Marcellus", serif;
    font-size: 72px;
    line-height: 1;
    letter-spacing: 5px;
    color: var(--brand-grey);
  }
  .brand-tagline {
    font-family: "Questrial", sans-serif;
    font-size: 24px;
    letter-spacing: 8px;
    color: var(--brand-olive);
    margin-top: 14px;
    white-space: nowrap;
  }
  .product-photo {
    position: absolute;
    top: 366px;
    left: 0;
    width: 100%;
    height: 330px;
    background: linear-gradient(180deg, var(--linen-light) 0%, var(--linen) 60%, var(--linen-warm) 100%);
    border-bottom: 3px solid var(--olive-dark);
  }
  .details {
    position: absolute;
    top: 752px;
    left: 0;
    width: 100%;
    text-align: center;
    font-size: 30px;
    line-height: 35px;
    color: var(--ink-soft);
  }
  .details p {
    margin: 0 0 17px;
  }
  .details .label {
    color: var(--ink);
    -webkit-text-stroke: 0.7px var(--ink);
  }
  .rule {
    position: absolute;
    top: 1101px;
    left: 165px;
    width: 465px;
    height: 3px;
    background: var(--olive-dark);
  }
  .website {
    position: absolute;
    top: 1128px;
    left: 0;
    width: 100%;
    text-align: center;
    font-size: 32px;
    letter-spacing: 6px;
    color: #3f3f3f;
    -webkit-text-stroke: 0.9px #3f3f3f;
  }
</style>
</head>
<body>
  <main class="insert">
    <div class="side-wash"></div>
    <svg class="swoosh" viewBox="0 0 827 1200" aria-hidden="true">
      <path d="M0 310 C 200 240, 420 260, 827 160" fill="none" stroke="#ffffff" stroke-opacity="0.35" stroke-width="18"/>
      <path d="M0 1000 C 220 930, 460 960, 827 880" fill="none" stroke="#ffffff" stroke-opacity="0.3" stroke-width="22"/>
      <path d="M0 1080 C 260 1040, 520 1060, 827 1000" fill="none" stroke="#c9c48a" stroke-opacity="0.25" stroke-width="14"/>
    </svg>

    <header class="brand">
      <div class="brand-dot"></div>
      <div class="brand-words">
        <span class="brand-name">VELARDO</span>
        <span class="brand-tagline">SLEEP PRODUCTS</span>
      </div>
    </header>

    <div class="product-photo" role="img" aria-label="Photo of a smiling woman resting on white pillows and bedding"></div>

    <section class="details">
      <p><span class="label">Description:</span><br>440 Thread Count Egyptian<br>Cotton Pillow Cases</p>
      <p><span class="label">Quantity:</span> 2</p>
      <p><span class="label">Size of Pillow Case:</span> Standard</p>
      <p><span class="label">Descriptive Words:</span> Soft, Caress,<br>Smooth, Gentle</p>
    </section>

    <div class="rule"></div>
    <div class="website">www.velardo.com</div>
  </main>
</body>
</html>
```